Etiketten für Honiggläser gesucht
sehr kreativer Entwurf, in dem alle umfangreichen Vorgaben berücksichtigt wurden. q4472 ist sehr service- und lösungsorientiert. Arbeitet sehr schnell und exzellent.
Zielgruppe
Wir sind eine junge Hobbyimkerei und produzieren unsere eigenen Honigsorten. Zielgruppe ist jeder, der Honig mag.
Aufgabenstellung
Das zu entwerfende Etiketten_Design soll grundsätzlich ein „absoluter Hingucker“ werden, einen hohen Wiedererkennungswert besitzen, edel erscheinen und die Hochwertigkeit des Produktes zum Ausdruck bringen.
Im engeren Sinn sollen zwei voneinander unabhängige Etikettenteile entworfen werden, die aber im Design eine Einheit bilden sollen:
Beim ersten Teil handelt es sich um den sogenannten Gewährverschluss; er verbindet den Deckel mit dem Glas und zerreißt beim ersten Öffnen des Deckels. Der Gewährverschluss soll etwa 2 cm breit und 8 cm lang sein, und unter anderem von unserem Firmenlogo (siehe Datei) geziert werden. Bei dem Logo darf die Grafik und der Hintergrund in der Farbe variieren, und der Schriftzug kann entfallen, andere Änderungen dürfen jedoch nicht vorgenommen werden. Das Logo kann bei Bedarf gerne in anderen Dateiformaten zur Verfügung gestellt werden.
Den zweiten Teil stellt das eigentliche Produktetikett dar. Für dieses gibt es keine Größen- und Formvorgaben, allerdings müssen folgende Inhalte Berücksichtigung finden: Die Daten des Imkers (bitte folgende Platzhalter verwenden „Firmenname“, „Vorname1 & Vorname2 Nachname“, „Straße + Hausnummer“, „PLZ + Ortsname“, „Internetseite“ und „Emailadresse“) sowie den Angaben „500g“, „Mindestens haltbar bis:“ (dahinter oder darunter bitte weißen Freiraum für den Stempelaufdruck des Datums lassen), „Trocken, dunkel und vor Wärme geschützt lagern!“, und – ganz wichtig – die „Honigsorte“ mit den vorangestellten Worten „feinster deutscher“ (, z.B. „feinster deutscher Rapshonig“).
Jede Honigsorte soll mit einer Farbe verknüpft werden, sodass der Kunde schnell erkennen kann um welche Honigsorte es sich im Glas handelt (beispielsweise gelb für Rapshonig, grün für Waldhonig, usw.). Dafür soll die jeweilige Honigsortenfarbe, in welcher Form auch immer, das Etikett oder einen bestimmten Bereich davon domini..

```html
<!DOCTYPE html>
<html lang="de">
<head>
<meta charset="utf-8">
<title>Imkerei Hollmann – Waldhonig Etikett</title>
<link href="https://fonts.googleapis.com/css2?family=Cinzel:wght@700&family=Dancing+Script:wght@600&family=Playfair+Display:ital@1&family=Source+Sans+3:wght@400&display=swap" rel="stylesheet">
<style>
  :root {
    --ink: #1f1f1f;
    --paper: #ffffff;
    --forest-deep: #1a8c45;
    --forest: #4a8c5e;
    --trim: #ffffff;
    --date-red: #e01010;
    --frame-grey: #555555;
  }
  html, body {
    margin: 0;
    padding: 0;
    width: 1200px;
    height: 848px;
    overflow: hidden;
    background: var(--paper);
  }
  .label {
    display: block;
    width: 1200px;
    height: 848px;
  }
  .brand-mark { fill: none; stroke: var(--ink); stroke-width: 9; }
  .brand-name {
    font-family: "Cinzel", serif;
    font-weight: 700;
    fill: var(--ink);
  }
  .ribbon-body { fill: url(#ribbonShade); }
  .ribbon-trim { fill: none; stroke: var(--trim); stroke-width: 5; stroke-linejoin: miter; }
  .variety {
    font-family: "Dancing Script", cursive;
    font-weight: 600;
    font-size: 104px;
    fill: var(--trim);
  }
  .weight {
    font-family: "Playfair Display", serif;
    font-style: italic;
    font-size: 40px;
    fill: var(--trim);
  }
  .contact, .storage, .bbd-label, .bbd-date {
    font-family: "Source Sans 3", sans-serif;
    font-weight: 400;
  }
  .contact { font-size: 25px; fill: var(--ink); }
  .storage { font-size: 24px; fill: #2a2a2a; }
  .bbd-label { font-size: 20px; fill: #333333; }
  .bbd-frame { fill: var(--paper); stroke: var(--frame-grey); stroke-width: 1.5; }
  .bbd-date { font-size: 25px; fill: var(--date-red); }
</style>
</head>
<body>
<svg class="label" viewBox="836 268 1203 850" xmlns="http://www.w3.org/2000/svg" role="img" aria-label="Etikett Waldhonig der Imkerei Hollmann">
  <defs>
    <linearGradient id="ribbonShade" x1="0" y1="0" x2="1" y2="0">
      <stop offset="0" stop-color="var(--forest-deep)"/>
      <stop offset="0.35" stop-color="var(--forest)"/>
      <stop offset="1" stop-color="var(--forest)"/>
    </linearGradient>
  </defs>

  <g class="brand">
    <circle class="brand-mark" cx="1425" cy="440" r="128"/>
    <text class="brand-name" x="1427" y="641" font-size="58" text-anchor="middle" textLength="345" lengthAdjust="spacing">IMKEREI</text>
    <text class="brand-name" x="1427" y="719" font-size="74" text-anchor="middle" textLength="345" lengthAdjust="spacingAndGlyphs">HOLLMANN</text>
  </g>

  <g class="ribbon">
    <path class="ribbon-body" d="M970,822 Q1437,682 1905,822 L1790,862 L1862,957 Q1437,807 1012,957 L1062,868 Z"/>
    <path class="ribbon-trim" d="M1000,826 Q1437,698 1872,826 L1772,862 L1838,940 Q1437,822 1034,940 L1088,864 Z"/>
    <text class="weight" x="1155" y="866" text-anchor="middle" textLength="104" lengthAdjust="spacingAndGlyphs">500G.</text>
    <text class="variety" x="1440" y="860" text-anchor="middle" textLength="348" lengthAdjust="spacingAndGlyphs">Waldhonig</text>
    <text class="weight" x="1722" y="862" text-anchor="middle" textLength="104" lengthAdjust="spacingAndGlyphs">500G.</text>
  </g>

  <g class="details">
    <text class="contact" x="1442" y="939" text-anchor="middle">Lindenweg 14 ● 4410 Talheim</text>
    <text class="contact" x="1442" y="973" text-anchor="middle">www.imkerei-hollmann.de ● kontakt@imkerei-hollmann.de</text>
    <text class="storage" x="1446" y="1017" text-anchor="middle">Trocken, dunkel und vor Wärme geschützt lagern</text>
    <text class="bbd-label" x="1423" y="1075" text-anchor="end">Mindestens haltbar bis:</text>
    <rect class="bbd-frame" x="1441" y="1041" width="226" height="43" rx="4"/>
    <text class="bbd-date" x="1554" y="1073" text-anchor="middle">17/11/2020</text>
  </g>
</svg>
</body>
</html>
```